Stationery Design for Pfotenhaus

We already have a logo a Logo for our outstanding veterinary hospital. Now we are looking for our future letterhead, business cards and envelopes. We would like to see a design using the color from our logo. Additional color should be limited to grey or a rusty brown. The font should be easy and clearly readable and must be easily available on all computers (to install it in our Management software). The finial design should communicate competence in veterinary medicine, and empathy.

To meet the European regulation (DIN5008) there are a couple mandatory legal informations one the letterhead. We also enclosed a template of exact measurement, which need to be respected according to DIN5008.

Mandatory legal information are (best placed in the footer):
"Pfotenhaus GmbH & Co KG, Brunnfeldgasse 417C, 1140 Wien,
Handelsgericht Wien, FN 294617k, GF: Dr. Lorenz Haidinger
ATU 3918462"
Additional informations needed:
"Tel: +43 1 5849162, Fax: +43 1 5849163, info@pfotenhaus-demo.at, www. pfotenhaus-demo.at"
bank account informations should be included as well. These are:
"Sparkasse Hollental Nord, IBAN: AT 58 1111 2222 3333 4444, BIC: HLNTAT2H517"

The Logo should be in the upper right corner. Below that we need a space for informations regarding the responsible veterinarians. There will be 3-5 Names, each of it consisting of 2 lines (see example below). The Names should be highlighted (larger font) compared to the qualifications in the second line.
Tierärztliche Leitung:
Dr. Lorenz Haidinger
Diplomate ECVS
Updates

The contest was startet on the 2nd of may and the deadline was a day later? Why was that so fast? Did I do something wrong? BR

Target Market(s)

dog and cat owner in Austria as welle as referring veterinarians in Austria

Industry/Entity Type

Veterinary

Contact Information for Business Card

One side: Logo
other side:
Dr. Lorenz Haidinger
Diplomate ECVS
EBVS Specialist of Small Animal Surgery

Pfotenhaus GmbH&Co KG
Brunnfeldgasse 417C
1140 Wien

Tel: +43 1 5849160 DW 102
Fax: +43 1 5849160 DW 999
email: lorenz.haidinger@pfotenhaus-demo.at

Font styles to use
Serif
Sans Serif

Requirements
Must have
• The logo should be given in the upper right. Most of the legal informations should be given in the footer. The upper left Area should be clear, since the recipient address will be placed there.
Colors should be limited to golden, blue and greyscale (two different gereysacales at most).

```html
<!DOCTYPE html>
<html lang="de">
<head>
<meta charset="utf-8">
<title>Pfotenhaus – Briefpapier</title>
<link href="https://fonts.googleapis.com/css2?family=Open+Sans:wght@400&family=Roboto:wght@400;500;700&display=swap" rel="stylesheet">
<style>
  :root {
    --navy: #1b2a55;
    --gold: #d4a627;
    --ink: #1f1f1f;
    --body-grey: #555555;
    --footer-grey: #666666;
    --paper: #f8f8f8;
    --backdrop: #dedede;
  }
  * { box-sizing: border-box; margin: 0; padding: 0; }
  html, body {
    width: 1153px; height: 1200px; overflow: hidden;
    background: var(--backdrop);
  }
  .letterhead {
    position: absolute; left: 160px; top: 20px;
    width: 1008px; height: 1406px;
    background: var(--paper);
    transform: scale(0.825); transform-origin: top left;
    box-shadow: 0 12px 40px rgba(0,0,0,0.12);
  }
  .brand {
    position: absolute; left: 556px; top: 101px;
    display: flex; align-items: center; gap: 12px;
  }
  .brand-dot {
    width: 102px; height: 102px; border-radius: 50%;
    background: var(--navy);
  }
  .brand-name {
    font-family: "Roboto", sans-serif; font-weight: 700;
    font-size: 40px; color: var(--navy); letter-spacing: 0.5px;
  }
  .vet-block {
    position: absolute; left: 91px; top: 264px;
    font-family: "Roboto", sans-serif; font-weight: 500;
    color: var(--ink); line-height: 31px;
  }
  .vet-name { font-size: 25px; }
  .vet-title { font-size: 24px; font-weight: 500; }
  .letter-body {
    position: absolute; left: 91px; top: 442px; width: 825px;
    font-family: "Open Sans", sans-serif; font-size: 18.8px;
    line-height: 27.2px; color: var(--body-grey);
  }
  .letter-body p { text-align: justify; margin-bottom: 27px; }
  .letter-body .salutation { margin-bottom: 27px; }
  .closing {
    position: absolute; left: 91px; top: 957px;
    font-family: "Open Sans", sans-serif; font-size: 18.8px; color: var(--body-grey);
  }
  .signature-area {
    position: absolute; left: 91px; top: 1010px; width: 120px; height: 110px;
    background: linear-gradient(135deg, #e9e9e9, #f3f3f3);
    border-radius: 4px;
  }
  .legal-footer {
    position: absolute; left: 0; top: 1233px; width: 100%;
    text-align: center; font-family: "Roboto", sans-serif;
    font-size: 20.5px; line-height: 26px; color: var(--footer-grey);
  }
  .legal-footer .bank { margin-top: 4px; }
  .contact-band {
    position: absolute; left: 0; top: 1333px; width: 100%; height: 46px;
    background: var(--navy);
  }
  .contact-band .accent {
    position: absolute; right: 0; top: 0; width: 90px; height: 100%;
    background: var(--gold);
  }
  .contact-band .band-dot {
    position: absolute; left: 893px; top: -6px; width: 58px; height: 58px;
    border-radius: 50%; background: var(--navy); border: 3px solid #fff;
  }
  .contact-list {
    position: absolute; left: 40px; top: 0; height: 100%;
    display: flex; align-items: center; gap: 9px;
    font-family: "Roboto", sans-serif; font-size: 19px; color: #fff;
    list-style: none; white-space: nowrap;
  }
  .contact-list li { display: flex; align-items: center; gap: 5px; }
  .contact-list svg { width: 18px; height: 18px; fill: var(--gold); }
</style>
</head>
<body>
  <main class="letterhead">
    <header class="brand">
      <span class="brand-dot"></span>
      <span class="brand-name">PFOTENHAUS</span>
    </header>

    <section class="vet-block">
      <div class="vet-name">Dr. Lorenz Haidinger</div>
      <div class="vet-title">Diplomate ECVS</div>
    </section>

    <article class="letter-body">
      <div class="salutation">Dear customer,</div>
      <p>Lorem ipsum dolor sit amet, consectetur adipisicing elit, sed do eiusmod tempor incididunt ut labore et dolore magna aliqua. Ut enim ad minim veniam, quis nostrud exercitation ullamco laboris nisi ut aliquip ex ea commodo consequat. Duis aute irure dolor in reprehenderit in voluptate velit esse cillum dolore eu fugiat nulla pariatur. Excepteur sint occaecat cupidatat non proident, sunt in culpa qui officia deserunt mollit anim id est laborum.</p>
      <p>Lorem ipsum dolor sit amet, consectetur adipisicing elit, sed do eiusmod tempor incididunt ut labore et dolore magna aliqua. Ut enim ad minim veniam, quis nostrud exercitation ullamco laboris nisi ut aliquip ex ea commodo consequat. Duis aute irure dolor in reprehenderit in voluptate velit esse cillum dolore eu fugiat nulla pariatur. Excepteur sint occaecat cupidatat non proident, sunt in culpa qui officia deserunt mollit anim id est laborum.</p>
      <p>Lorem ipsum dolor sit amet, consectetur adipisicing elit, sed do eiusmod tempor incididunt ut labore et dolore magna aliqua. Ut enim ad minim veniam, quis nostrud exercitation ullamco laboris nisi ut aliquip ex ea commodo consequat.</p>
    </article>

    <div class="closing">Yours Sincerely,</div>
    <div class="signature-area" role="img" aria-label="Handwritten signature of the veterinarian"></div>

    <footer class="legal-footer">
      <div>Pfotenhaus GmbH &amp; Co KG, Brunnfeldgasse 417C, 1140 Wien,</div>
      <div>Handelsgericht Wien, FN 294617k, GF: Dr. Lorenz Haidinger ATU 3918462</div>
      <div class="bank">Sparkasse Hollental Nord IBAN: AT 58 1111 2222 3333 4444 BIC: HLNTAT2H517</div>
    </footer>

    <div class="contact-band">
      <span class="accent"></span>
      <span class="band-dot"></span>
      <ul class="contact-list">
        <li>
          <svg viewBox="0 0 20 20" aria-hidden="true"><path d="M2 7c0-2 3-4 8-4s8 2 8 4v2h-4V7.5c-1-.6-2.5-.8-4-.8s-3 .2-4 .8V9H2z"/><path d="M5 10h10l2 6H3z"/></svg>
          +43 1 5849162
        </li>
        <li>
          <svg viewBox="0 0 20 20" aria-hidden="true"><rect x="5" y="2" width="10" height="5"/><rect x="2" y="7" width="16" height="7" rx="1"/><rect x="5" y="12" width="10" height="6"/></svg>
          +43 1 5849163
        </li>
        <li>
          <svg viewBox="0 0 20 20" aria-hidden="true"><path d="M2 5h16v10H2z"/><path d="M2 5l8 6 8-6" fill="none" stroke="#1b2a55" stroke-width="1.5"/></svg>
          info@pfotenhaus-demo.at
        </li>
        <li>
          <svg viewBox="0 0 20 20" aria-hidden="true"><circle cx="10" cy="10" r="8"/><path d="M6 6c2 0 2 2 4 2s1 3-1 3-2 3-3 1-2-4 0-6zM12 12c2 0 3 1 2 3-1 1-3 0-2-3z" fill="#1b2a55"/></svg>
          www.pfotenhaus-demo.at
        </li>
      </ul>
    </div>
  </main>
</body>
</html>
```